Business Card Design Project

Business card for new event planning company. I will load in 2 different colors of logs for you to use.

Target Market(s)

meeting planners and business leaders

Industry/Entity Type

Event Planning

Requirements
Must have
• memorable/ creative please - maybe logo on back of the card

Information for business card: (Information may change)

LaVonna Pettibrook
lav@MarigoldOccasionsandGalas.com
www.MarigoldOccasionsandGalas.com
613.275.9042
Nice to have
• Do you think it would be too much to add chirpy, QX, workmesh logo to card to connect?

all are LaVonna Pettibrook

```html
<!DOCTYPE html>
<html lang="en">
<head>
<meta charset="utf-8">
<title>Marigold Occasions &amp; Galas – Business Card</title>
<link rel="stylesheet" href="https://fonts.googleapis.com/css2?family=Overlock:wght@400;700&display=swap">
<style>
  :root {
    --page: #e6e3df;
    --card-dark: #2b2a30;
    --card-dark-pattern: #36353c;
    --panel-light: #eeeef1;
    --panel-pattern: #e4e4e9;
    --lavender: #8f7fd6;
    --ink: #2a2a2e;
    --ink-soft: #3a3a40;
  }
  * { box-sizing: border-box; margin: 0; padding: 0; }
  html, body { width: 1200px; height: 900px; overflow: hidden; }
  body {
    background: var(--page);
    font-family: "Overlock", sans-serif;
    color: var(--ink);
    position: relative;
  }
  .card {
    position: absolute;
    left: 300px;
    width: 600px;
    height: 343px;
    border-radius: 4px;
    box-shadow: 0 6px 18px rgba(0,0,0,.18);
    overflow: hidden;
  }

  /* Back of card */
  .card--back { top: 66px; background: var(--card-dark); }
  .card--back .pattern {
    position: absolute; inset: 0;
    background: radial-gradient(circle at 50% 50%, var(--card-dark-pattern), var(--card-dark) 75%);
  }
  .card--back .frame {
    position: absolute; inset: 16px;
    border: 1.5px solid var(--lavender);
    border-radius: 3px;
  }
  .card--back .brand {
    position: absolute; inset: 0;
    display: flex; align-items: center; justify-content: center;
    font-size: 46px; font-weight: 700;
    color: var(--lavender);
  }

  /* Front of card */
  .card--front { top: 490px; background: var(--card-dark); }
  .card--front .panel {
    position: absolute; inset: 14px;
    background: var(--panel-light);
    border: 2px solid var(--lavender);
    border-radius: 6px;
    overflow: hidden;
  }
  .panel .pattern {
    position: absolute; inset: 0;
    background: radial-gradient(circle at 40% 50%, var(--panel-light), var(--panel-pattern));
  }
  .panel .brand {
    position: absolute; left: 22px; top: 120px; width: 200px;
    font-size: 25px; font-weight: 700; line-height: 1.05;
    color: var(--lavender);
  }
  .panel .divider {
    position: absolute; left: 240px; top: 80px;
    width: 1.5px; height: 132px; background: var(--lavender);
  }
  .panel .holder {
    position: absolute; right: 48px; top: 96px;
    font-size: 24px; color: var(--ink);
  }
  .contact {
    position: absolute; right: 26px; top: 150px;
    list-style: none; text-align: right;
    font-size: 15.5px; line-height: 20px; color: var(--ink-soft);
  }
  .contact li { display: flex; align-items: center; justify-content: flex-end; gap: 8px; }
  .contact svg { width: 11px; height: 11px; flex: none; }
  .social {
    position: absolute; right: 26px; bottom: 38px;
    display: flex; align-items: center; gap: 10px;
    font-size: 15px; color: var(--ink-soft);
  }
  .social .handle { margin-right: 8px; }
  .social .network { display: flex; align-items: center; gap: 4px; font-size: 13px; }
  .social .network::before {
    content: ""; width: 10px; height: 10px; border-radius: 2px; background: var(--lavender);
  }
</style>
</head>
<body>

  <section class="card card--back" aria-label="Business card back">
    <div class="pattern" role="img" aria-label="Faint dark paisley pattern"></div>
    <div class="frame"></div>
    <div class="brand">Marigold Occasions&amp;Galas</div>
  </section>

  <section class="card card--front" aria-label="Business card front">
    <div class="panel">
      <div class="pattern" role="img" aria-label="Soft light grey paisley pattern"></div>
      <div class="brand">Marigold Occasions&amp;Galas</div>
      <div class="divider"></div>
      <div class="holder">LaVonna Pettibrook</div>
      <ul class="contact">
        <li>613.275.9042
          <svg viewBox="0 0 12 12"><path fill="#8f7fd6" d="M2.5 1l2 2-1 1.3a6 6 0 0 0 4.2 4.2l1.3-1 2 2-1.3 1.5C5 10.5 1.5 7 1 2.3z"/></svg></li>
        <li>lav@MarigoldOccasionsandGalas.com
          <svg viewBox="0 0 12 12"><rect x="1" y="2.5" width="10" height="7" fill="none" stroke="#8f7fd6" stroke-width="1.2"/><path d="M1 2.5l5 4 5-4" fill="none" stroke="#8f7fd6" stroke-width="1.2"/></svg></li>
        <li>www.MarigoldOccasionsandGalas.com
          <svg viewBox="0 0 12 12"><path fill="#8f7fd6" d="M6 0.5a3.8 3.8 0 0 1 3.8 3.8C9.8 7 6 11.5 6 11.5S2.2 7 2.2 4.3A3.8 3.8 0 0 1 6 .5z"/><circle cx="6" cy="4.3" r="1.4" fill="#eeeef1"/></svg></li>
      </ul>
      <div class="social">
        <span class="handle">LaVonna Pettibrook</span>
        <span class="network">chirpy</span>
        <span class="network">QX</span>
        <span class="network">workmesh</span>
      </div>
    </div>
  </section>

</body>
</html>
```